Tri-fold Brochure Design for Law Firm

I need a tri-fold brochure to give to prospective clients.
I have attached a Photoshop design file of a tri-fold brochure. The content (copy) is good, however, he brochure itself looks very amateurish.
I want a professional, sophisticated looking brochure.
The law firm specializes in commercial debt collection.
The law firm is located in New York City.
Our target market is business owners, doctors, lawyers, collection agencies and accountants.
Visit my website which is being designed at www.dorvenlaw.com. I like the font used for the name of my company and the rich blue color used.

Target Market(s)

Business Owners, Doctors, Law Firms and Accountants

Industry/Entity Type

Law Firm

Font styles to use
Serif

Requirements
Must have
• Professional quality graphic work. Attention to details.
• PHOTOGRAPHS ONLY, NO CLIP-ART.
• DARK COLORS - NAVY BLUE, HUNTER GREEN, BLACK, GRAY & WHITE
Nice to have
• I want it to look smart, modern and sophisticated.
• Visit my website which is being designed at www.dorvenlaw.com. I like the font used for the name of my company and the rich blue color used.
Should not have
• Bad artwork
• CLIP ART

```html
<!DOCTYPE html>
<html lang="en">
<head>
<meta charset="utf-8">
<title>Marcello Dorven &amp; Company, PLLC — Tri-fold Brochure</title>
<link rel="stylesheet" href="https://fonts.googleapis.com/css2?family=Marcellus+SC&family=Open+Sans:wght@400;600;700;800&display=swap">
<style>
  :root{
    --backdrop:#141414;
    --navy:#0c1a6e;
    --navy-deep:#081255;
    --royal:#1d3fb5;
    --sky:#1f8ee6;
    --cyan:#1fb6ec;
    --paper:#f2f3f7;
    --ink:#1d2240;
    --title-blue:#1a2f96;
    --white:#ffffff;
  }
  *{box-sizing:border-box;margin:0;padding:0}
  html,body{width:1200px;height:900px;overflow:hidden;background:var(--backdrop)}
  body{font-family:"Open Sans",Arial,sans-serif;color:var(--white)}
  .brochure{position:absolute;left:48px;top:30px;width:1104px;height:840px;display:flex;box-shadow:0 20px 50px rgba(0,0,0,.6)}
  .panel{position:relative;width:368px;height:840px;overflow:hidden;background:var(--navy)}
  .panel + .panel{border-left:1px solid rgba(0,0,0,.25)}
  .abs{position:absolute}
  .wave{position:absolute;left:0;width:368px}

  .band-top{left:0;top:0;width:368px;background:linear-gradient(135deg,var(--navy-deep),var(--royal));}
  .footer{left:0;bottom:0;width:368px;height:108px;background:linear-gradient(135deg,var(--navy-deep),var(--navy) 60%,var(--royal));border-top:4px solid var(--cyan)}

  .heading{font-weight:700;font-size:21px;line-height:1.25;letter-spacing:.3px}
  .body-copy{font-size:12.5px;line-height:1.3}
  .paper{background:var(--paper);color:var(--ink)}
  .paper .heading{color:var(--title-blue)}

  .photo{background:linear-gradient(160deg,#9aa3ad,#d9dde2 40%,#5b6470 75%,#2c3340)}
  .photo-court{background:linear-gradient(180deg,#2f6fd0 0%,#6ea6e6 45%,#e8ecef 72%,#b9bec4 100%)}

  .toll{width:368px;text-align:center;top:28px}
  .toll small{display:block;font-weight:700;font-size:14px;letter-spacing:.5px}
  .toll strong{font-weight:800;font-size:30px;letter-spacing:.5px}

  .seal{left:129px;top:300px;width:110px;height:110px;border-radius:50%;background:var(--white);border:5px solid #dfe4f2;display:flex;align-items:center;justify-content:center;color:var(--title-blue);font-size:17px;font-weight:600;letter-spacing:1px}
  .firm-line{width:368px;text-align:center;font-family:"Marcellus SC",Georgia,serif;font-size:21px;top:432px}
  .tagline{width:368px;text-align:center;font-size:13px;top:460px}
  .contact{width:368px;text-align:center;font-size:13px;line-height:1.35}
  .contact b{font-weight:700;font-size:16px}
  .office-label{color:var(--cyan);font-weight:700;text-decoration:underline;font-size:13px}
  .icon{display:inline-block;vertical-align:-2px;margin-right:4px}

  .web-row{width:368px;text-align:center;top:22px;font-size:16px;font-weight:700}
  .phone-row{width:368px;top:56px;display:flex;justify-content:center;gap:22px;font-weight:800;font-size:17px}

  .cover-name{top:170px;width:368px;text-align:center;font-family:"Marcellus SC",Georgia,serif;font-weight:400;color:var(--title-blue);font-size:42px;line-height:1.1}
  .cover-tag{width:368px;text-align:center;top:38px;font-weight:800;font-size:20px;letter-spacing:.3px}
</style>
</head>
<body>
<div class="brochure">

  <section class="panel panel-left">
    <div class="abs band-top" style="height:128px;padding:18px 22px 0 26px">
      <h2 class="heading">WHO WE ARE</h2>
      <p class="body-copy" style="margin-top:4px"><b>MARCELLO DORVEN &amp; COMPANY, PLLC (DORVEN)</b> is a New York based Law Firm devoted to the collection of accounts receivable and business debts.</p>
    </div>
    <div class="abs photo" role="img" aria-label="Photo of smiling business people in suits shaking hands" style="left:0;top:128px;width:368px;height:172px"></div>
    <div class="abs paper" style="left:0;top:300px;width:368px;height:440px"></div>
    <svg class="wave" style="top:270px" width="368" height="60" viewBox="0 0 368 60" aria-hidden="true">
      <path d="M0 40 C110 20 250 10 368 20 L368 34 C250 26 120 34 0 56 Z" fill="var(--sky)"/>
      <path d="M0 52 C120 32 250 26 368 32 L368 36 C250 30 120 38 0 58 Z" fill="var(--navy)"/>
    </svg>
    <div class="abs paper" style="left:0;top:322px;width:368px;padding:0 24px 0 26px;background:transparent">
      <h2 class="heading">WHAT WE DO</h2>
      <p class="body-copy" style="margin-top:4px">Within 24 to 72 hours of receiving a claim, we will verify the debt, investigate the Debtor, skip trace all known stakeholders and file a lawsuit with the intent of collecting the full amount due in the shortest time possible.</p>
      <p class="body-copy" style="margin-top:9px">We will use all legal means necessary to locate, identify, seize, or otherwise garnish a Debtor's assets and income, while always having an attorney available to speak directly with the Debtor to achieve an amicable resolution as quickly as possible.</p>
      <h2 class="heading" style="margin-top:9px">OUR MISSION</h2>
      <p class="body-copy" style="margin-top:3px">Our mission is to protect our clients' bottom line, while preserving their reputation.</p>
      <p class="body-copy" style="margin-top:8px">We recognize and appreciate that your Debtor was once a trusted customer and may be a source of future revenue.</p>
      <p class="body-copy" style="margin-top:8px">We treat all Debtors with respect, while aggressively seeking to collect all monies owed.</p>
    </div>
    <div class="abs footer">
      <div class="abs toll"><small>TOLL FREE</small><strong>877 555 0190</strong></div>
    </div>
  </section>

  <section class="panel panel-centre">
    <div class="abs band-top" style="height:112px;padding:16px 24px 0 26px">
      <h2 class="heading">WHY USE US</h2>
      <p class="body-copy" style="margin-top:4px">Anyone can sue a Debtor. It's not difficult to get nasty or to treat people who owe you money in a rude and unprofessional way.</p>
    </div>
    <div class="abs" style="left:0;top:112px;width:368px;height:4px;background:var(--cyan)"></div>
    <div class="abs" style="left:0;top:116px;width:368px;height:626px;background:linear-gradient(180deg,var(--navy-deep),var(--navy) 40%,var(--royal) 100%)"></div>
    <div class="abs body-copy" style="left:26px;top:130px;width:318px">
      <p>However, very few people have the skill, temperament and experience needed to effectively negotiate with Debtors, stakeholders, lawyers, as well as, court personnel, sheriffs and bankers to efficiently collect the most money possible in the least amount of time.</p>
      <p style="margin-top:10px">We truly understand the nature of commercial debt. Collecting money is our specialized skill.</p>
    </div>
    <svg class="wave" style="top:282px" width="368" height="150" viewBox="0 0 368 150" aria-hidden="true">
      <path d="M0 0 C90 8 200 30 368 70 L368 120 C230 84 110 70 0 74 Z" fill="var(--sky)"/>
      <path d="M0 74 C110 70 230 84 368 120 L368 128 C230 92 110 80 0 82 Z" fill="var(--white)"/>
    </svg>
    <div class="abs seal">DORVEN</div>
    <div class="abs firm-line">Marcello Dorven &amp; Company, PLLC</div>
    <div class="abs tagline">Debt Collection Attorneys in New York State</div>
    <div class="abs contact" style="top:490px">
      <b>MARCELLO J. DORVEN, ESQUIRE</b><br>President<br>
      <span style="font-weight:700"><svg class="icon" width="14" height="11" viewBox="0 0 14 11" aria-hidden="true"><rect x="0.5" y="0.5" width="13" height="10" fill="none" stroke="#fff"/><path d="M0.5 0.5 L7 6 L13.5 0.5" fill="none" stroke="#fff"/></svg>mdorven@dorvenlaw.com</span><br>
      <span style="font-weight:700"><svg class="icon" width="10" height="13" viewBox="0 0 10 13" aria-hidden="true"><rect x="0.5" y="0.5" width="9" height="12" rx="1.5" fill="none" stroke="#fff"/><line x1="3" y1="10" x2="7" y2="10" stroke="#fff"/></svg>212.555.0147</span>
    </div>
    <div class="abs contact" style="top:584px">
      <span class="office-label">WESTCHESTER COUNTY OFFICE</span><br>
      410 Harbor Ridge Road, Suite 210<br>White Plains, New York 10604<br>(Off Exit 4 on Route 12 East)
    </div>
    <div class="abs contact" style="top:664px">
      <span class="office-label">MAILING ADDRESS</span><br>
      516 Linden Avenue, Suite 2080<br>New York, New York 10016-0000
    </div>
    <div class="abs footer">
      <div class="abs web-row"><svg class="icon" width="15" height="15" viewBox="0 0 16 16" aria-hidden="true"><circle cx="8" cy="8" r="7" fill="none" stroke="#fff" stroke-width="1.4"/><ellipse cx="8" cy="8" rx="3" ry="7" fill="none" stroke="#fff" stroke-width="1.2"/><line x1="1" y1="8" x2="15" y2="8" stroke="#fff" stroke-width="1.2"/></svg>www.dorvenlaw.com</div>
      <div class="abs phone-row">
        <span><svg class="icon" width="16" height="14" viewBox="0 0 16 14" aria-hidden="true"><path d="M1 5 C1 1 15 1 15 5 L12 6 L11 4 L5 4 L4 6 Z" fill="#fff"/><rect x="3" y="7" width="10" height="6" rx="1" fill="none" stroke="#fff"/></svg>212 555 0163</span>
        <span><svg class="icon" width="16" height="14" viewBox="0 0 16 14" aria-hidden="true"><rect x="1" y="5" width="14" height="8" rx="1" fill="none" stroke="#fff"/><rect x="4" y="1" width="8" height="4" fill="none" stroke="#fff"/><line x1="4" y1="9" x2="12" y2="9" stroke="#fff"/></svg>917 555 0128</span>
      </div>
    </div>
  </section>

  <section class="panel panel-cover">
    <div class="abs band-top" style="height:100px"></div>
    <div class="abs" style="left:0;top:100px;width:368px;height:4px;background:var(--royal)"></div>
    <div class="abs paper" style="left:0;top:104px;width:368px;height:260px;background:linear-gradient(180deg,#ffffff,var(--paper))"></div>
    <h1 class="abs cover-name">Marcello Dorven<br>&amp;<br>Company, PLLC</h1>
    <div class="abs photo-court" role="img" aria-label="Photo of a classical columned courthouse under a blue sky with an American flag" style="left:0;top:400px;width:368px;height:340px"></div>
    <svg class="wave" style="top:330px" width="368" height="120" viewBox="0 0 368 120" aria-hidden="true">
      <path d="M0 0 C100 20 220 40 368 30 L368 84 C230 96 110 84 0 70 Z" fill="var(--sky)"/>
      <path d="M0 70 C110 84 230 96 368 84 L368 92 C230 104 110 92 0 78 Z" fill="var(--white)"/>
    </svg>
    <div class="abs footer">
      <div class="abs cover-tag">DEBT COLLECTION ATTORNEYS</div>
    </div>
  </section>

</div>
</body>
</html>
```